Website, Logo, & Ppt Look & Feel Revamp for a small growth strategy firm

We haven't updated the look and feel of our company (http://brv-plano.com/) in a few years and it's not so impressive anymore. It's also frustrating that we currently work with only blue-scale colors and that makes designing eye-catching powerpoints a challenge. The design must indicate "growth" and an understanding of business ecosystem.
We prefer minimalist designs, as part of what we don't like about our current site is that the pages are crowded.
Note: **We would like to move away from a purely blue-scale look!** All ideas welcome.
Target Market(s)
Customers include B2B and professional services firms
Industry/Entity Type
Business
Look and feel
Each slider illustrates characteristics of the customer's brand and the style your logo design should communicate.

```html
<!DOCTYPE html>
<html lang="en">
<head>
<meta charset="utf-8">
<title>Plano Growth — Home</title>
<link href="https://fonts.googleapis.com/css2?family=Noto+Serif:ital,wght@0,700;1,400&family=Open+Sans:wght@400;700&display=swap" rel="stylesheet">
<style>
  :root {
    --brand: #d4004c;
    --ink: #333333;
    --paper: #ffffff;
    --night-dark: #1a0c08;
    --night-warm: #6b2a14;
    --night-glow: #c0392b;
  }
  * { margin: 0; padding: 0; box-sizing: border-box; }
  html, body {
    width: 1200px; height: 1000px; overflow: hidden;
    background: var(--paper);
    font-family: "Open Sans", Arial, sans-serif;
    color: var(--ink);
  }
  .page { width: 1000px; margin: 0 auto; position: relative; }
  .site-header { height: 100px; display: flex; justify-content: space-between; align-items: stretch; }
  .brand-name {
    display: flex; align-items: center; gap: 10px;
    font-weight: 700; font-size: 20px; color: var(--brand);
  }
  .brand-square { width: 22px; height: 22px; background: var(--brand); }
  .main-nav { display: flex; align-items: stretch; }
  .main-nav a {
    display: flex; align-items: center;
    padding: 0 17px; margin-left: 2px;
    font-weight: 700; font-size: 15px; text-transform: uppercase;
    color: var(--ink); text-decoration: none;
  }
  .main-nav a:last-child { padding-right: 0; }
  .main-nav a.is-current { background: var(--brand); color: var(--paper); margin-right: 1px; }
  .hero {
    margin-top: 30px; height: 320px; position: relative; overflow: hidden;
    background:
      linear-gradient(180deg, rgba(0,0,0,0) 60%, rgba(200,40,40,.55) 100%),
      linear-gradient(180deg, var(--night-warm) 0%, var(--night-dark) 25%, #2b120a 55%, var(--night-glow) 100%);
  }
  .hero-tile { position: absolute; width: 100px; background: rgba(212,0,76,.45); top: 0; }
  .hero-tile.light { background: rgba(255,210,190,.35); }
  .hero-title {
    position: absolute; left: 0; right: 0; top: 146px;
    text-align: center;
    font-family: "Noto Serif", Georgia, serif; font-style: italic; font-weight: 400;
    font-size: 44px; line-height: 60px; color: var(--paper);
    text-shadow: 2px 2px 3px rgba(0,0,0,.9);
  }
  .content { padding-top: 29px; }
  .content h1 {
    font-family: "Noto Serif", Georgia, serif; font-weight: 700;
    font-size: 34px; color: var(--brand); line-height: 1.2; margin-bottom: 18px;
  }
  .content p { font-size: 16.7px; line-height: 23px; margin-bottom: 23px; }
</style>
</head>
<body>
  <div class="page">
    <header class="site-header">
      <div class="brand-name"><span class="brand-square"></span>Plano Growth</div>
      <nav class="main-nav">
        <a class="is-current" href="#">Home</a>
        <a href="#">About Us</a>
        <a href="#">People</a>
        <a href="#">Clients</a>
        <a href="#">Services</a>
        <a href="#">Insights</a>
        <a href="#">Contact Us</a>
      </nav>
    </header>

    <section class="hero" role="img" aria-label="Aerial photograph of a city skyline at night with glowing red and amber lights">
      <div class="hero-tile" style="left:400px;height:160px;"></div>
      <div class="hero-tile light" style="left:600px;height:80px;"></div>
      <h2 class="hero-title">Re-Thinking Your Core Business for Growth</h2>
    </section>

    <main class="content">
      <h1>This is a content heading</h1>
      <p>Lorem ipsum dolor sit amet, at usu odio cibo intellegat, odio error referrentur ad mel. Denique fierent per cu. Usu utinam consequat at, fabulas partiendo sea ut. Adhuc atomorum at duo.</p>
      <p>At hinc legendos mei, et vim singulis reprimique. Pri liberavisse suscipiantur at, mel id graeco contentiones. Cu ius zril putent eloquentiam. Nec in congue fabellas quaestio. Nam audiam tractatos scribentur ea.</p>
      <p>Elit quodsi indoctum et per, quod noster accommodare ad vel. Mea suavitate iudicabit complectitur cu. Ut nam dicat reprehendunt, choro democritum interesset at sed. Ancillae scaevola suscipiantur pro ne. Eu docendi deterruisset eum, te mel sumo aeterno denique, wisi offendit hendrerit ex eos. Purto omnis graece usu an, paulo lobortis persequeris eu eum, id usu labore principes.</p>
      <p>Eu utinam sanctus euripidis est, his eu tamquam sanctus scribentur. Ius suas facilisis adversarium te, timeam patrioque prodesset vel at. Et omnium consectetuer vel, vel ei falli admodum laboramus. Nam apeirian delicatissimi an, ubique dignissim voluptaria duo ea. Qui quidam docendi assentior ex, vis te primis urbanitas eloquentiam. In ferri brute legimus eam.</p>
    </main>
  </div>
</body>
</html>
```